Announcement for a New Trauma Therapy Group - Rack Card

I need a two-sided "rack" card that is 4x9 announcing a Women's Trauma and Loss Group. I am a licensed therapist and will be starting this support group for women who have experienced trauma of all kinds. In addition to groups, I offer individual, couples, and family counseling sessions.

I would like to see designs that are soft tones and use colors like muted blues, greens, and sand tones. The final design should communicate hope and healing as well as have a peaceful feel to it.

I would like a picture of a woman's profile from either the side or from behind her. (possibly a contemplative picture on a beach)

I am attaching a picture of myself to go alongside the bio information as well.

On One Side, I need the description of the group and contact info:

Mending the Weary Spirit
Women's Trauma & Loss Group
Led by Licensed Professional Counselor, Jen Dalby Rusk

10 Week Group
Cost - $35 session
Group size limited to 10 participants

Topics Include:
What is Trauma?
How Trauma Affects Us
Creating a Feeling of Safety
Managing Trauma Triggers
Importance of Self Care
Healthy vs. Unhealthy Coping
Guilt, Shame, and Blame
Victim vs. Victimized
Grieving through Loss
Anger and Forgiveness
Imagining a Better Future

For More Information, Contact:
Jen Dalby Rusk, LPC, LMFT
(555) 614-3920
jen@brightmeadowcare.example

On Side Two:

Life hurts and does not seem fair. So what do you do when you are faced with an event in your life that knocks you off your feet? It seems no one understands what you are feeling and no one knows just what to say. It is tempting to pull away and isolate or put up a mask and pretend everything is OK.

It is my desire you know that you are not alone! There are others who understand the feelings you are going through and offer a safe place for encouraging support. I want to invite you to embark on a courageous journey of healing where you will not only learn how to "survive" after trauma and loss, but instead, learn that you can once again "thrive"!
- Jen Dalby Rusk, LPC, LMFT

Jen Dalby Rusk is a Licensed Professional Counselor and Licensed Marriage and Family Therapist. She is the owner of Quiet Harbor Counseling Services located in Tulsa, OK.

Jen is a trauma survivor herself and understands firsthand the unique challenges that can arise on the journey to healing.

(Include Jen's picture next to bio)

(Attach logo and business information to this side as well.)

Target Market(s)

Women who have gone through a traumatic experience or loss and are hurting emotionally

Industry/Entity Type

Counsellor

Font styles to use
Serif
Script

Colors
fbe7d2
86cfc6
cfeae6
85abd2
cfdeed

Requirements
Must have
• Jen's picture as well as her logo and contact information must be on the card.
• One side of the card should describe the group with the following description:
• "Mending the Weary Spirit"
• Women's Trauma & Loss Group
• Led by Licensed Professional Counselor, Jen Dalby Rusk
• 10 Week Group
• Cost - $35 session
• Group size limited to 10 participants
• Topics Include:
• What is Trauma?
• How Trauma Affects Us
• Creating a Feeling of Safety
• Managing Trauma Triggers
• Importance of Self Care
• Healthy vs. Unhealthy Coping
• Guilt, Shame, and Blame
• Victim vs. Victimized
• Grieving through Loss
• Anger and Forgiveness
• Imagining a Better Future
• For More Information, Contact:
• Jen Dalby Rusk, LPC, LMFT
• (555) 614-3920
• jen@brightmeadowcare.example
• On the second side, it must have this note from Jen:
• Life hurts and does not seem fair. So what do you do when you are faced with an event in your life that knocks you off your feet? It seems no one understands what you are feeling and no one knows just what to say. It is tempting to pull away and isolate or put up a mask and pretend everything is OK.
• It is my desire you know that you are not alone! There are others who understand the feelings you are going through and offer a safe place for encouraging support. I want to invite you to embark on a courageous journey of healing where you will not only learn how to "survive" after trauma and loss, but instead, learn that you can once again "thrive"!
• - Jen Dalby Rusk, LPC, LMFT
• Jen Dalby Rusk is a Licensed Professional Counselor and Licensed Marriage and Family Therapist. She is the owner of Quiet Harbor Counseling Services located in Tulsa, OK.
• Jen is a trauma survivor herself and understands firsthand the unique challenges that can arise on the journey to healing. In addition to facilitating groups, Jen also offers individual, marriage, and family counseling.
Nice to have
• soft muted colors that are peaceful. Light blues, greens, sand colors would work well. A picture at the top of the card of either a woman or a woman's profile that is hopeful such as a woman sitting at a beach overlooking the ocean.
Should not have
• No harsh or bright bold colors. This card needs to have a peaceful feeling to it.

```html
<!DOCTYPE html>
<html lang="en">
<head>
<meta charset="utf-8">
<title>Mending the Weary Spirit – Rack Card</title>
<link href="https://fonts.googleapis.com/css2?family=Roboto:ital,wght@0,300;0,400;0,500;1,500;1,700&family=Roboto+Condensed:ital,wght@0,400;1,700&family=Ubuntu:wght@500&family=Great+Vibes&display=swap" rel="stylesheet">
<style>
  :root {
    --backdrop: #c4c4c4;
    --sky-blue: #4ba9ca;
    --title-blue: #47a6c6;
    --sage: #7fb495;
    --sage-light: #9dcfb0;
    --mist: #ececee;
    --ink: #2c2c2c;
    --ink-soft: #3d3d3d;
    --dot: #4ba9ca;
    --white: #ffffff;
  }
  * { margin: 0; padding: 0; box-sizing: border-box; }
  html, body { width: 1200px; height: 1200px; overflow: hidden; }
  body { background: var(--backdrop); position: relative; font-family: "Roboto", sans-serif; color: var(--ink); }

  .rack-card { position: absolute; top: 125px; width: 437px; height: 950px; overflow: hidden; box-shadow: 0 3px 10px rgba(0,0,0,.25); }
  .rack-card--front { left: 137px; background: var(--mist); }
  .rack-card--back { left: 642px; background: linear-gradient(to bottom, var(--sky-blue) 0%, #bfe0ec 45%, #ffffff 62%); }

  /* front */
  .hero-photo { position: absolute; left: 0; top: 0; width: 437px; height: 404px;
    background: linear-gradient(to bottom, #e3edf3 0%, #cfdeea 22%, #5f8fb0 30%, #7ea5c0 42%, #d9d4c8 58%, #e3dccf 100%); }
  .brand-mark { position: absolute; left: 226px; top: 70px; display: flex; align-items: center; gap: 8px; }
  .brand-mark__dot { width: 22px; height: 22px; border-radius: 50%; background: #4f8a3a; }
  .brand-mark__name { font-family: "Roboto", sans-serif; font-weight: 500; font-size: 17px; line-height: 1.1; color: #2f4f2a; width: 110px; }

  .sage-rule { position: absolute; left: 0; top: 404px; width: 100%; height: 6px; background: var(--sage); }
  .title-band { position: absolute; left: 0; top: 410px; width: 100%; height: 100px; background: var(--white); text-align: center; color: var(--title-blue); font-weight: 500; }
  .title-band__line1 { font-size: 31px; letter-spacing: 1px; margin-top: 10px; line-height: 1; }
  .title-band__line2 { font-size: 41px; letter-spacing: 1px; margin-top: 8px; line-height: 1; }

  .group-band { position: absolute; left: 0; top: 510px; width: 100%; height: 62px; background: var(--sage); text-align: center; color: var(--white); border-bottom: 3px solid #6aa283; }
  .group-band__name { font-family: "Ubuntu", sans-serif; font-weight: 500; font-size: 21px; margin-top: 8px; }
  .group-band__lead { font-family: "Roboto Condensed", sans-serif; font-size: 14.5px; margin-top: 2px; }

  .details { position: absolute; left: 0; top: 572px; width: 100%; height: 299px;
    background: linear-gradient(to bottom, var(--mist) 0%, var(--mist) 60%, #bfe0ec 82%, #5eb3d0 100%); text-align: center; }
  .details__weeks { font-size: 37px; font-weight: 500; color: var(--sage); margin-top: 20px; line-height: 1; }
  .details__cost { font-size: 19px; font-weight: 400; margin-top: 6px; }
  .details__cost em { font-style: italic; font-weight: 700; }
  .details__limit { font-size: 19.5px; margin-top: 2px; }

  .topics-heading { position: absolute; left: 0; top: 122px; width: 100%; height: 30px; }
  .topics-heading__rule { position: absolute; top: 14px; height: 1px; background: var(--sage); }
  .topics-heading__rule--left { left: 0; width: 150px; }
  .topics-heading__rule--right { right: 0; width: 155px; }
  .topics-heading__dot { position: absolute; top: 11px; width: 7px; height: 7px; border-radius: 50%; background: #4a7d5f; }
  .topics-heading__text { font-family: "Great Vibes", cursive; font-size: 22px; color: #4a7d5f; line-height: 30px; }

  .topic-list { position: absolute; top: 158px; list-style: none; text-align: left; font-size: 11.6px; color: var(--ink-soft); }
  .topic-list li { height: 21.5px; position: relative; padding-left: 11px; }
  .topic-list li::before { content: ""; position: absolute; left: 0; top: 6px; width: 4px; height: 4px; border-radius: 50%; background: var(--dot); }
  .topic-list--left { left: 36px; }
  .topic-list--right { left: 250px; }
  .topic-divider { position: absolute; left: 220px; top: 160px; width: 1px; height: 130px; background: #b9c3c6; }

  .contact-footer { position: absolute; left: 0; top: 871px; width: 100%; height: 79px; border-top: 3px solid var(--white); }
  .rack-card--front .contact-footer { background: var(--sky-blue); }
  .rack-card--back .contact-footer { background: var(--sage-light); }
  .contact-footer__pill { position: absolute; left: 50%; top: -13px; transform: translateX(-50%); background: var(--white); border-radius: 8px; padding: 4px 10px; font-size: 9.8px; font-weight: 500; white-space: nowrap; }
  .rack-card--front .contact-footer__pill { color: var(--sage); }
  .rack-card--back .contact-footer__pill { color: var(--sky-blue); }
  .contact-footer__col { position: absolute; top: 20px; font-size: 9.6px; color: #26343a; white-space: nowrap; }
  .contact-footer__col--left { left: 31px; }
  .contact-footer__col--right { left: 270px; }
  .contact-footer__row { display: flex; align-items: center; gap: 6px; height: 16px; }
  .contact-footer__row svg { width: 9px; height: 9px; flex: none; }
  .contact-footer__split { position: absolute; left: 222px; top: 18px; width: 1px; height: 32px; background: rgba(255,255,255,.7); }

  /* back */
  .quote-frame { position: absolute; left: 24px; top: 24px; width: 389px; height: 847px; border: 1.5px solid var(--white); }
  .letter { position: absolute; left: 41px; width: 352px; font-size: 14.6px; font-weight: 300; line-height: 17px; text-align: justify; color: #1f2a30; }
  .letter p + p { margin-top: 13px; }
  .letter--quote { top: 51px; }
  .letter--bio { top: 365px; }
  .quote-mark { font-family: "Roboto", sans-serif; font-style: italic; font-weight: 700; font-size: 26px; line-height: 0; color: var(--white); }
  .quote-mark--open { position: absolute; left: -3px; top: 14px; }
  .quote-mark--close { display: inline-block; margin-left: 12px; transform: translateY(12px); }
  .letter__first { text-indent: 24px; }
  .signature { position: absolute; left: 41px; top: 300px; width: 352px; text-align: right; font-family: "Roboto Condensed", sans-serif; font-style: italic; font-weight: 700; font-size: 14.2px; color: #1f2a30; }
  .portrait-photo { position: absolute; left: 0; top: 555px; width: 437px; height: 316px;
    background: linear-gradient(to bottom, #7d8a6c 0%, #b9ad93 20%, #a99b86 35%, #8f8a84 70%, #7b7774 100%); }
</style>
</head>
<body>

<section class="rack-card rack-card--front">
  <div class="hero-photo" role="img" aria-label="Woman in a white sweater sitting on a sandy beach, seen from behind, looking out over the ocean"></div>
  <div class="brand-mark">
    <span class="brand-mark__dot"></span>
    <span class="brand-mark__name">Quiet Harbor Counseling</span>
  </div>
  <div class="sage-rule"></div>
  <header class="title-band">
    <div class="title-band__line1">MENDING THE</div>
    <div class="title-band__line2">WEARY SPIRIT</div>
  </header>
  <div class="group-band">
    <div class="group-band__name">Women's Trauma &amp; Loss Group</div>
    <div class="group-band__lead">Led by Licensed Professional Counselor, Jen Dalby Rusk</div>
  </div>
  <div class="details">
    <div class="details__weeks">10 WEEK GROUP</div>
    <div class="details__cost">COST - <em>$35 SESSION</em></div>
    <div class="details__limit">Group size limited to 10 participants</div>
    <div class="topics-heading">
      <span class="topics-heading__rule topics-heading__rule--left"></span>
      <span class="topics-heading__dot" style="left:147px"></span>
      <span class="topics-heading__text">Topics Include:</span>
      <span class="topics-heading__dot" style="right:152px"></span>
      <span class="topics-heading__rule topics-heading__rule--right"></span>
    </div>
    <ul class="topic-list topic-list--left">
      <li>What is Trauma?</li>
      <li>How Trauma Affects Us</li>
      <li>Creating a Feeling of Safety</li>
      <li>Managing Trauma Triggers</li>
      <li>Importance of Self Care</li>
      <li>Healthy vs. Unhealthy Coping</li>
    </ul>
    <span class="topic-divider"></span>
    <ul class="topic-list topic-list--right">
      <li>Guilt, Shame, and Blame</li>
      <li>Victim vs. Victimized</li>
      <li>Grieving through Loss</li>
      <li>Anger and Forgiveness</li>
      <li>Gratitude and Spirituality</li>
      <li>From Tragedy to Triumph!</li>
    </ul>
  </div>
  <footer class="contact-footer">
    <span class="contact-footer__pill">For More Information, Contact</span>
    <div class="contact-footer__col contact-footer__col--left">
      <div class="contact-footer__row"><svg viewBox="0 0 10 10"><circle cx="5" cy="5" r="5" fill="#fff"/><circle cx="5" cy="4" r="1.8" fill="#4ba9ca"/><path d="M2 8.3a3 3 0 0 1 6 0z" fill="#4ba9ca"/></svg>Jen Dalby Rusk, LPC, LMFT</div>
      <div class="contact-footer__row"><svg viewBox="0 0 10 10"><path d="M2 1l2 2-1 1.2c.6 1.3 1.5 2.2 2.8 2.8L7 6l2 2-1.3 1.3C4.5 9 1 5.5.7 2.3z" fill="#fff"/></svg>(555) 614-3920</div>
    </div>
    <span class="contact-footer__split"></span>
    <div class="contact-footer__col contact-footer__col--right">
      <div class="contact-footer__row"><svg viewBox="0 0 10 10"><circle cx="5" cy="5" r="5" fill="#fff"/><rect x="2.5" y="3.3" width="5" height="3.4" fill="none" stroke="#4ba9ca" stroke-width=".8"/></svg>jen@brightmeadowcare.example</div>
      <div class="contact-footer__row"><svg viewBox="0 0 10 10"><circle cx="5" cy="5" r="5" fill="#fff"/><circle cx="5" cy="5" r="3" fill="none" stroke="#4ba9ca" stroke-width=".8"/></svg>www.quietharbor.example</div>
    </div>
  </footer>
</section>

<section class="rack-card rack-card--back">
  <div class="quote-frame"></div>
  <div class="letter letter--quote">
    <span class="quote-mark quote-mark--open">“</span>
    <p class="letter__first">Life hurts and is not always fair. So what do you do when you are faced with an event in your life that knocks you off your feet? It seems no one understands what you are feeling and no one knows just what to say. It is tempting to pull away and isolate or put up a mask and pretend everything is OK.</p>
    <p>It is my desire you know that you are not alone! There are others who understand the feelings you are going through and offer a safe place for encouraging support. I want to invite you to embark on a courageous journey of healing where you will not only learn how to "survive" after trauma and loss, but instead, learn that you can once again "thrive"!<span class="quote-mark quote-mark--close">”</span></p>
  </div>
  <div class="signature">- Jen Dalby Rusk, LPC, LMFT</div>
  <div class="letter letter--bio">
    <p>Jen Dalby Rusk is a Licensed Professional Counselor and Licensed Marriage and Family Therapist. She is the owner of Quiet Harbor Counseling Services located in Tulsa, OK.</p>
    <p>Jen is a trauma survivor herself and understands firsthand the unique challenges that can arise on the journey to healing. In addition to facilitating groups, Jen offers individual, marriage, and family counseling.</p>
  </div>
  <div class="portrait-photo" role="img" aria-label="Portrait of the counselor sitting on a rock on a beach at sunset with dunes and stairs behind her"></div>
  <footer class="contact-footer">
    <span class="contact-footer__pill">For More Information, Contact</span>
    <div class="contact-footer__col contact-footer__col--left">
      <div class="contact-footer__row"><svg viewBox="0 0 10 10"><circle cx="5" cy="5" r="5" fill="#fff"/><circle cx="5" cy="4" r="1.8" fill="#9dcfb0"/><path d="M2 8.3a3 3 0 0 1 6 0z" fill="#9dcfb0"/></svg>Jen Dalby Rusk, LPC, LMFT</div>
      <div class="contact-footer__row"><svg viewBox="0 0 10 10"><path d="M2 1l2 2-1 1.2c.6 1.3 1.5 2.2 2.8 2.8L7 6l2 2-1.3 1.3C4.5 9 1 5.5.7 2.3z" fill="#fff"/></svg>(555) 614-3920</div>
    </div>
    <span class="contact-footer__split"></span>
    <div class="contact-footer__col contact-footer__col--right">
      <div class="contact-footer__row"><svg viewBox="0 0 10 10"><circle cx="5" cy="5" r="5" fill="#fff"/><rect x="2.5" y="3.3" width="5" height="3.4" fill="none" stroke="#9dcfb0" stroke-width=".8"/></svg>jen@brightmeadowcare.example</div>
      <div class="contact-footer__row"><svg viewBox="0 0 10 10"><circle cx="5" cy="5" r="5" fill="#fff"/><circle cx="5" cy="5" r="3" fill="none" stroke="#9dcfb0" stroke-width=".8"/></svg>www.quietharbor.example</div>
    </div>
  </footer>
</section>

</body>
</html>
```